Changes to wine label

Need existing labels designed by Pixel Harbor corrected to meet QRV.

Target Market(s)

Wine drinkers

Requirements
Must have
• Use attached label design. A. Label #2 spelling correct" Zinfandel". Also, 500ml instead of 375ml and place on front label with so would be 500ml/Alcohol %18 By Volume. Remove residual sugar text.
Should not have
• Sorrel Bluff LOGO on both label#1 & #2 different red that pops the log. And an addtional label with the white grapes

```html
<!DOCTYPE html>
<html lang="en">
<head>
<meta charset="utf-8">
<title>Sorrel Bluff Mead Co – Wine Labels</title>
<link href="https://fonts.googleapis.com/css2?family=Old+Standard+TT:ital,wght@0,400;0,700;1,400&family=Arimo:ital,wght@0,400;0,700;1,400&display=swap" rel="stylesheet">
<style>
  :root {
    --bg-top: #f8f8f9;
    --bg-bottom: #bcc0c7;
    --label-black: #000000;
    --label-glow: #2e2e2e;
    --brand-red: #9a1634;
    --text-white: #ffffff;
    --grape-light: #d98ad8;
    --grape-dark: #6a2a66;
    --seal-gold: #c9a544;
    --seal-gold-dark: #a88428;
  }
  * { margin: 0; padding: 0; box-sizing: border-box; }
  html, body { width: 1200px; height: 1043px; overflow: hidden; }
  body {
    position: relative;
    background: linear-gradient(to bottom, var(--bg-top), var(--bg-bottom));
    font-family: "Arimo", Arial, sans-serif;
    color: var(--text-white);
  }
  .label {
    position: absolute;
    width: 395px;
    height: 473px;
    background: var(--label-black);
    overflow: hidden;
  }
  .label-glow {
    position: absolute;
    inset: 0;
    background: radial-gradient(ellipse 55% 45% at 50% 52%, var(--label-glow), var(--label-black) 100%);
  }
  .label--front { left: 190px; top: 203px; }
  .label--back { left: 615px; top: 367px; }

  .brand-name {
    position: absolute;
    left: 0; right: 0;
    text-align: center;
    font-family: "Old Standard TT", Georgia, serif;
    font-weight: 400;
    color: var(--brand-red);
    letter-spacing: 3px;
    line-height: 1.15;
    text-transform: uppercase;
  }
  .label--front .brand-name { top: 92px; font-size: 25px; }
  .label--back .brand-name { top: 50px; font-size: 19px; }

  .grape-art {
    position: absolute;
    left: 93px; top: 190px;
    width: 210px; height: 188px;
    border-radius: 45% 55% 50% 50%;
    background: radial-gradient(circle at 45% 45%, var(--grape-light), var(--grape-dark));
  }
  .volume-line {
    position: absolute;
    left: 0; right: 0; top: 428px;
    text-align: center;
    font-size: 13.5px;
    letter-spacing: 1px;
  }

  .origin {
    position: absolute;
    left: 0; right: 0; top: 116px;
    text-align: center;
    font-family: "Old Standard TT", Georgia, serif;
    font-size: 13px;
    line-height: 16px;
  }
  .description {
    position: absolute;
    left: 10px; right: 10px; top: 155px;
    text-align: center;
    font-family: "Old Standard TT", Georgia, serif;
    font-size: 16px;
    line-height: 19.8px;
    letter-spacing: 0.3px;
  }
  .producer {
    position: absolute;
    left: 0; right: 0; top: 271px;
    text-align: center;
    font-style: italic;
    font-size: 9.5px;
    line-height: 11.5px;
    text-transform: uppercase;
  }
  .warning {
    position: absolute;
    left: 17px; right: 15px; top: 310px;
    font-size: 12.2px;
    line-height: 17.5px;
  }
  .warning strong { font-weight: 700; letter-spacing: 0.3px; }
  .volume-small, .sulfites {
    position: absolute;
    top: 406px;
    font-size: 11px;
  }
  .volume-small { left: 17px; }
  .sulfites { right: 17px; }
  .seal {
    position: absolute;
    left: 173px; top: 410px;
    width: 48px; height: 48px;
    border-radius: 50%;
    background: radial-gradient(circle at 40% 35%, var(--seal-gold), var(--seal-gold-dark));
  }
</style>
</head>
<body>
  <section class="label label--front">
    <div class="label-glow"></div>
    <div class="brand-name">Sorrel Bluff<br>Mead Co</div>
    <div class="grape-art" role="img" aria-label="Illustration of a bunch of purple grapes on a stem"></div>
    <p class="volume-line">500ml/Alcohol %18 By Volume</p>
  </section>

  <section class="label label--back">
    <div class="label-glow"></div>
    <div class="brand-name">Sorrel Bluff<br>Mead Co</div>
    <p class="origin">CALIFORNIA<br>ZINFANDEL 50% SYRAH 50%</p>
    <p class="description">A fruit forward dessert style wine that<br>takes the aroma of the varitals and balances<br>it with sweetness and zealous acidity.<br>Meant to be drunk young or slightly aged,<br>complementary with cheeses and chocolate.</p>
    <p class="producer">Produced and bottles by<br>Sorrel Bluff Mead Co. Alder Springs, California</p>
    <p class="warning"><strong>GOVERNMENT WARNING:</strong>(1) According to the Surgeon General, women should not drink alcoholic beverages during pregnancy because of the risk of birth defects. (2) Consumption of alcoholic beverages impairs your ability to drive a car or operate machinery, and may cause health problems.</p>
    <p class="volume-small">500ML</p>
    <p class="sulfites">CONTAINS SULFITES</p>
    <div class="seal"></div>
  </section>
</body>
</html>
```